Business Card Design Project

New business cards that encompass our new logo.
Looking for -
Name, Title, Cell Phone, Email, Address (2 lines), Main Phone, Fax, and website.
Reason: I don't like the graphics used to show phone, fax, cell, email, web, and address.....
I like the double sided cards with logo's on the back. I do not like the logos for phone, fax, cell, address, email, or web.

```html
<!DOCTYPE html>
<html lang="en">
<head>
<meta charset="utf-8">
<title>Northpeak Restaurant Supply – Business Card</title>
<link rel="stylesheet" href="https://fonts.googleapis.com/css2?family=Lato:wght@400;700;900&family=Open+Sans:wght@700&display=swap">
<style>
  :root {
    --backdrop: #6b6b6b;
    --card: #ffffff;
    --navy: #1f3f8a;
    --red: #c23a4b;
  }
  * { margin: 0; padding: 0; box-sizing: border-box; }
  html, body {
    width: 1200px; height: 900px; overflow: hidden;
    background: var(--backdrop);
  }
  .card {
    position: absolute; left: 120px; top: 175px;
    width: 960px; height: 550px;
    background: var(--card);
    font-family: "Lato", sans-serif;
    overflow: hidden;
  }
  .brand {
    position: absolute; left: 80px; top: 100px;
    display: flex; align-items: center; gap: 16px;
    color: var(--navy);
    font-weight: 900;
    line-height: 1;
    text-transform: uppercase;
  }
  .brand-square { width: 20px; height: 20px; background: var(--navy); flex: none; }
  .brand-name { font-size: 60px; letter-spacing: 1px; }
  .brand-name small { display: block; font-size: 22px; letter-spacing: 2.4px; margin-top: 6px; }
  .person {
    position: absolute; right: 62px; top: 140px; text-align: right;
  }
  .person-name {
    font-size: 44px; font-weight: 400; color: var(--navy); letter-spacing: 0.5px; line-height: 1.1;
  }
  .person-title {
    font-size: 16px; font-weight: 700; color: var(--red); letter-spacing: 1px;
    text-transform: uppercase; margin-top: 4px;
  }
  .contacts {
    position: absolute; left: 80px; top: 262px;
    list-style: none;
  }
  .contact {
    display: flex; align-items: center; gap: 18px;
    font-size: 26px; color: var(--navy); height: 40px;
  }
  .contact::before {
    content: ""; width: 9px; height: 9px; background: var(--red); flex: none;
  }
  .address-band {
    position: absolute; left: 0; bottom: 0; width: 100%; height: 74px;
    background: var(--red);
    display: flex; align-items: center; padding-left: 70px;
    font-family: "Open Sans", sans-serif; font-weight: 700;
    font-size: 26px; color: #fff; letter-spacing: 0.6px;
  }
</style>
</head>
<body>
<main class="card">
  <div class="brand">
    <span class="brand-square"></span>
    <span class="brand-name">Northpeak<small>Restaurant Supply</small></span>
  </div>

  <div class="person">
    <p class="person-name">DANA HOLLIS</p>
    <p class="person-title">Title goes here</p>
  </div>

  <ul class="contacts">
    <li class="contact">0912-448-207</li>
    <li class="contact">dana@northpeaksupply.com</li>
    <li class="contact">555-014-2290</li>
    <li class="contact">555-014-2291</li>
    <li class="contact">www.northpeaksupply.com</li>
  </ul>

  <footer class="address-band">418 Harbor Lane, Suite #303, Ridge Bldg, NY 10541</footer>
</main>
</body>
</html>
```